A new website is needed for a breakthrough creative thinking tool

My name is Ross Malden - i have a PhD in Organisational Creativity and have written a few books on creative & Rapid Musing. You can check me out by visiting www.drrossmalden.example

I have uncovered an amazing insight of what stops most people from being more creative.

Themselves.

They filter & judge their own rich, new ideas. I have found the best way to overcome this self-limiting behaviour is to encourage people to think of ideas really quickly so they have no time to judge - they just create.

I call this accelerated form of creativity - Rapid Musing and the tool i have developed is Notion Sprint. There are 5 steps - Start, enhance, connect, evaluate & action.

The most important step is the start where i ask each person to create 9 ideas in 2 minutes using a visual bubble format (see the uploaded file). For many people this magic formula (my wording) is the very essence of an Notion Sprint.

I have also developed a new mobile app (phone & tablet) which you can find here -

http://lnk.example/7QpRz2K

I wish to develop a new word press site which promotes Notion Sprint.

My vision is to have all the world Sprinting. In a time-poor world where students, managers, leaders & small business owners are being asked to be more creative, innovative and do more with less - we need better, faster tools.

Notion Sprint is an ideal tool for this new world.

I passionately believe in the power of Notion Sprint to unlock amazing creativity in the most logical of people.

I have tested this new tool with thousands of people across Australia, Asia and the US.

I would like to develop a web site which is as creative as the tool itself. My aim is top create a site that explains the concept of an Notion Sprint through the use of videos, blogs and refer visitors to the new mobile app.

I would like this site to be talked about and help to create a movement of Sprinters around the world.

Notion Sprint is the next great creative thinking tool after Brainstorming (developed 70 years ago) & Mindmapping (developed 30 years ago).

Notion Sprint can be used by an individual, partner or group.

The key benefits of using an Notion Sprint are:
- It is a simple, practical, effective way of unlocking the creativity of everyone.
- Notion Sprint is fast & time efficient.
- It helps people who procrastinate to get started (some 20-25% of the adult population are chronic procrastinators; 70% plus for students).
- It enables everyone in group work to contribute their ideas because each person has to create 9 ideas in 2 minutes
- People feel more confident and energised and
- It accelerates progress
Updates

this brief is for a design only

someone else will build the word press site
thanks ross

Reason: Some of the designs are close but require some more work as per my feedback. thanks ross

As part of my requirements i would also like to see 2-3 website pages other than the homepage.

thanks ross

Target Market(s)

This is a mass market product.

But it is a new concept.

Think how Cerebrica is trying to position and sell their brain training games.

Any student, manager, leader or small business owner can use this tool/app.

In large organisations it would engage and interest anyone involved in marketing, innovation, advertising, research, HR, new product development, customer service, training, sales etc.

The people who are most interested in my work have a particular mindset - they are open to new ideas, want to challenge the status quo, welcome change, like learning, sharing and collaborating.

The other segment are those people who are interested in helping others to reach their potential e.g. teachers, trainers, facilitators, coaches etc.

Industry/Entity Type

Small Business

Requirements
Must have
• The Notion Sprint web site design should be clean, simple and answer the following questions:

- What is an Notion Sprint? A breakthrough thinking tool and app that overcomes the biggest barrier that stops most people from being more creative ( or reaching their full creative potential) - i.e. their own internal judging, critical voice.

It's your mobile creative system.

- Who should Sprint? High School right through to university students, small business owners, managers & leaders.

When to Sprint: You can Sprint at any time - in a bus, train, subway, work in the class room. But here are some specific examples
- In a brainstorming, ideation, planning session
- In group work
- You can use as a weekly to do list
- When you need to solve a problem or generate an idea
- You have a flash of inspiration and want to capture an idea or make an existing idea 9 times better
- To do an initial structure an essay, project, assignment, presentation or speech.
- To summarise a topic etc etc etc
Nice to have
• I have an existing web site www.drrossmalden.example

It might be useful to have a potential visual link with this site but this is a nice to have.

The bubbles (see the uploaded file) are an important part of the Notion Sprint tool so this might be worth highlighting in some way (the bubbles help users to make connections and escape thinking in a logical, structured, list type way).

```html
<!DOCTYPE html>
<html lang="en">
<head>
<meta charset="utf-8">
<title>Dr Ross Malden – Notion Sprint</title>
<link rel="stylesheet" href="https://fonts.googleapis.com/css2?family=Oswald:wght@300;400;500&family=PT+Sans+Narrow:wght@400;700&display=swap">
<style>
:root{
  --ink:#31323f;
  --bubble:#5b5c68;
  --bubble-ring:#9c9da6;
  --paper:#ececec;
  --card:#ffffff;
  --text:#2b2b2b;
  --muted:#5e5e5e;
  --orange:#f3961c;
  --blue:#1b9fd6;
  --red:#e21d3c;
  --green:#5e9c2b;
  --grey:#c7c7c7;
  --line:#9a9a9a;
  --promo:#d8d8d8;
}
*{box-sizing:border-box;margin:0;padding:0}
html,body{width:1200px;height:2637px;overflow:hidden}
body{background:var(--paper);font-family:"PT Sans Narrow",Arial,sans-serif;color:var(--text);position:relative}

/* Header */
.site-header{position:absolute;left:0;top:0;width:1200px;height:805px;background:var(--ink)}
.brand{position:absolute;top:34px;left:0;width:1200px;text-align:center;color:#fff}
.brand-dot{display:block;width:26px;height:26px;border-radius:50%;border:2px solid #fff;margin:0 auto 12px}
.brand-name{font-family:"Oswald",sans-serif;font-weight:400;font-size:20px;letter-spacing:5px;line-height:1}
.main-nav{position:absolute;top:150px;left:71px;width:1058px;height:61px;display:flex}
.main-nav a{flex:1;display:flex;align-items:center;justify-content:center;color:#fff;text-decoration:none;font-family:"Oswald",sans-serif;font-size:13px;font-weight:400;text-transform:uppercase}
.nav-orange{background:var(--orange)}.nav-blue{background:var(--blue)}.nav-red{background:var(--red)}.nav-green{background:var(--green)}.nav-grey{background:var(--grey)}

.bubble{position:absolute;width:158px;height:158px;margin:-79px 0 0 -79px;border-radius:50%;background:var(--bubble);border:3px solid var(--bubble-ring);box-shadow:0 0 0 3px var(--ink),0 0 0 4px #464754;display:flex;align-items:center;justify-content:center;text-align:center;color:#fff;font-family:"Oswald",sans-serif;font-size:20px;line-height:1.25;padding:18px}
.bubble--start{background:#fff;color:var(--ink);border:5px solid var(--ink);box-shadow:0 0 0 5px #fff,0 0 0 6px #6a6b76}

/* Section headings */
.section-title{position:absolute;left:71px;width:1058px;display:flex;align-items:center;gap:24px;font-family:"Oswald",sans-serif;font-weight:500;font-size:26px;color:var(--text);text-transform:uppercase;white-space:nowrap}
.section-title::before,.section-title::after{content:"";flex:1;height:6px;border-top:1px solid var(--line);border-bottom:1px solid var(--line)}

/* Blog */
.post-card{position:absolute;top:915px;width:327px;height:403px;background:var(--card);display:flex;flex-direction:column}
.post-image{height:174px}
.post-body{flex:1;padding:24px 22px 0;text-align:center}
.post-title{font-family:"Oswald",sans-serif;font-weight:400;font-size:17px;line-height:1.25;text-transform:uppercase;color:var(--text)}
.post-date{font-size:14px;margin:8px 0 10px;color:var(--text)}
.post-date span{color:var(--red)}
.post-excerpt{font-size:12.5px;line-height:1.45;color:var(--muted)}
.post-more{height:44px;display:flex;align-items:center;justify-content:center;color:#fff;font-family:"Oswald",sans-serif;font-size:15px;text-transform:uppercase;text-decoration:none}

/* Welcome */
.welcome-copy{position:absolute;top:1422px;left:90px;width:1020px;text-align:center;font-size:14.5px;line-height:1.55}
.welcome-copy strong{font-weight:700}
.welcome-copy p+p{margin-top:16px}
.welcome-copy p.tight{margin-top:0}
.btn-blue{position:absolute;top:1593px;left:438px;width:327px;height:44px;background:var(--blue);color:#fff;display:flex;align-items:center;justify-content:center;font-family:"Oswald",sans-serif;font-size:15px;text-decoration:none}

/* Community */
.community{position:absolute;top:1701px;left:219px;width:765px;height:153px;background:var(--promo)}
.community h2{position:absolute;left:33px;top:22px;font-family:"Oswald",sans-serif;font-weight:500;font-size:37px;color:var(--ink);line-height:1}
.community p{position:absolute;left:33px;top:68px;font-size:17px;color:var(--blue)}
.community p strong{font-weight:700}
.signup{position:absolute;left:33px;top:104px;width:168px;height:34px;background:var(--red);color:#fff;display:flex;align-items:center;justify-content:center;font-family:"Oswald",sans-serif;font-size:15px;text-decoration:none}
.ebook-cover{position:absolute;left:584px;top:16px;width:90px;height:120px;background:linear-gradient(160deg,#ffffff,#e4e6ee 60%,#2c3f8f)}
.buy-now{position:absolute;left:652px;top:20px;width:78px;height:78px;border-radius:50%;background:var(--blue);border:3px solid #fff;color:#fff;display:flex;align-items:center;justify-content:center;text-align:center;font-family:"Oswald",sans-serif;font-size:17px;line-height:1}

/* Map */
.map{position:absolute;top:1957px;left:0;width:1200px;height:327px;background:linear-gradient(135deg,#e9e4d6,#f2efe6 45%,#dfe6cf)}

/* Footer */
.site-footer{position:absolute;top:2284px;left:0;width:1200px;height:353px;background:var(--ink);color:#fff;text-align:center}
.social{position:absolute;top:65px;left:0;width:1200px;display:flex;justify-content:center;gap:23px}
.social a{width:64px;height:64px;border-radius:50%;display:flex;align-items:center;justify-content:center;color:#fff;text-decoration:none;font-size:13px}
.social-a{background:#1f9fd6}.social-b{background:#3a5d9c}.social-c{background:#d9482f}
.to-top{position:absolute;top:265px;left:588px}
.footer-links{position:absolute;top:305px;left:0;width:1200px;font-size:13px;color:#e6e6ea}
.footer-links span{margin:0 8px;color:#8a8b95}
</style>
</head>
<body>

<header class="site-header">
  <div class="brand">
    <span class="brand-dot"></span>
    <div class="brand-name">DR ROSS MALDEN</div>
  </div>
  <nav class="main-nav">
    <a class="nav-orange" href="#">Home</a>
    <a class="nav-blue" href="#">Blog</a>
    <a class="nav-red" href="#">About Ross</a>
    <a class="nav-green" href="#">Tools</a>
    <a class="nav-grey" href="#">Speak</a>
    <a class="nav-orange" href="#">Consult</a>
    <a class="nav-blue" href="#">Facilitate</a>
    <a class="nav-red" href="#">Train</a>
    <a class="nav-green" href="#">NPD</a>
    <a class="nav-grey" href="#">Books</a>
    <a class="nav-orange" href="#">Contact</a>
  </nav>

  <div class="bubble" style="left:533px;top:309px">What is an Notion Sprint?</div>
  <div class="bubble" style="left:696px;top:309px">How to run a Sprint</div>
  <div class="bubble" style="left:414px;top:490px">The Challenge</div>
  <div class="bubble bubble--start" style="left:604px;top:490px">Start</div>
  <div class="bubble" style="left:788px;top:490px">Enhance</div>
  <div class="bubble" style="left:327px;top:662px">Connect</div>
  <div class="bubble" style="left:493px;top:662px">Evaluate</div>
  <div class="bubble" style="left:696px;top:662px">Action</div>
  <div class="bubble" style="left:881px;top:662px">When can you Sprint?</div>
</header>

<h2 class="section-title" style="top:842px">The latest from Dr Ross's blog</h2>

<article class="post-card" style="left:74px">
  <div class="post-image" role="img" aria-label="Photo of a teacher in front of a classroom with raised hands" style="background:linear-gradient(135deg,#3f6b45,#c9b79a 55%,#e7e1d6)"></div>
  <div class="post-body">
    <h3 class="post-title">To build an innovation culture you need more creative conversations</h3>
    <div class="post-date">Posted on <span>11/15/ 2013</span></div>
    <p class="post-excerpt">It is not enough to generate big, new ideas if no-one is open to them. Innovative cultures are built on the back of creative conversations. Here's how to conduct one.</p>
  </div>
  <a class="post-more" href="#" style="background:var(--red)">Read more</a>
</article>

<article class="post-card" style="left:438px">
  <div class="post-image" role="img" aria-label="Promotional graphic for the Notion Sprint creativity tool" style="background:linear-gradient(180deg,#f4f8fb,#cfe4f2)"></div>
  <div class="post-body">
    <h3 class="post-title">When to<br>call an Notion Sprint?</h3>
    <div class="post-date">Posted on <span style="color:var(--orange)">11/15/ 2013</span></div>
    <p class="post-excerpt">Notion Sprint is a powerful creative thinking tool we have developed – here is when to use it from an experienced HR professional.</p>
  </div>
  <a class="post-more" href="#" style="background:var(--orange)">Read more</a>
</article>

<article class="post-card" style="left:799px">
  <div class="post-image" role="img" aria-label="Photo of a glowing light bulb on a blue background" style="background:radial-gradient(circle at 55% 45%,#dff2ff,#3a8fd0 35%,#0b2c5c 80%)"></div>
  <div class="post-body">
    <h3 class="post-title">Is this the world's<br>smartest innovation program?</h3>
    <div class="post-date">Posted on <span style="color:var(--green)">11/15/ 2013</span></div>
    <p class="post-excerpt">Harlow Health Group in Australia are about to launch a program which has as its theme. The aim of the program is to highlight then stop the many dumb things that...</p>
  </div>
  <a class="post-more" href="#" style="background:var(--green)">Read more</a>
</article>

<h2 class="section-title" style="top:1356px">Welcome to Dr Ross Malden</h2>

<div class="welcome-copy">
  <p><strong>They filter &amp; judge their own rich, new ideas. I have found the best way to overcome this self-limiting behaviour is to encourage people to think of ideas really quickly so they have no time to judge - they just create. I call this accelerated form of creativity - Rapid Musing and the tool I have developed is Notion Sprint.</strong></p>
  <p>There are 5 steps - Start, enhance, connect, evaluate &amp; action.</p>
  <p class="tight">The most important step is the start where i ask each person to create 9 ideas in 2 minutes using a visual bubble format (see the uploaded file). For many people this magic formula (my wording) is the very essence of an Notion Sprint. I have also developed a new mobile app (phone &amp; tablet)</p>
</div>
<a class="btn-blue" href="#">READ MORE</a>

<section class="community">
  <h2>JOIN THE COMMUNITY</h2>
  <p>Sign up for regular updates and get a free E Book on <strong>36 innovation tips</strong></p>
  <a class="signup" href="#">SIGNUP NOW</a>
  <div class="ebook-cover" role="img" aria-label="Cover of the free innovation tips e-book"></div>
  <div class="buy-now">BUY<br>NOW</div>
</section>

<h2 class="section-title" style="top:1889px">Our location</h2>
<div class="map" role="img" aria-label="Street map showing the office location"></div>

<footer class="site-footer">
  <div class="social">
    <a class="social-a" href="#">Chirp</a>
    <a class="social-b" href="#">Folio</a>
    <a class="social-c" href="#">Circlo</a>
  </div>
  <div class="brand" style="top:180px">
    <span class="brand-dot"></span>
    <div class="brand-name">DR ROSS MALDEN</div>
  </div>
  <svg class="to-top" width="24" height="22" viewBox="0 0 24 22" aria-label="Back to top">
    <polyline points="3,10 12,2 21,10" fill="none" stroke="#fff" stroke-width="3"/>
    <polyline points="3,20 12,12 21,20" fill="none" stroke="#fff" stroke-width="3"/>
  </svg>
  <div class="footer-links">© Dr Ross Malden<span>|</span>Contact Dr Ross Malden<span>|</span>Privacy</div>
</footer>

</body>
</html>
```